Dental Specialist Needs a Business Card

We are a state of the art dental specialty office and need a business card that looks modern but professional.
I have provided our logo design in both vertical and horizontal. We use the design on letterhead in the vertical format but provided both forms for you. Thanks

Please add the address, phone and fax numbers I listed to all designs and please leave a space for website and for my employee name on each design. Thanks 2847 Halloway Avenue, Suite K East Marlow, NY 14391 Phone (716)382-9157 Fax:(716)382-9150 My name is Miles R.Dunford,D.D.S. If you want to show it with my name but the design needs to allow for the name to be switched.

Industry/Entity Type

Business

```html
<!DOCTYPE html>
<html lang="en">
<head>
<meta charset="utf-8">
<title>Keystone Endodontics P.C. – Business Card</title>
<link rel="stylesheet" href="https://fonts.googleapis.com/css2?family=Libre+Baskerville:wght@400;700&family=Open+Sans:wght@400;600&display=swap">
<style>
  :root{
    --page:#e9e7e3;
    --sky:#4fb3e3;
    --sky-deep:#2f9bd3;
    --sky-pale:#a9dcf3;
    --leaf:#8cc63f;
    --leaf-deep:#6cb02e;
    --ink:#111111;
    --text:#3a3a3a;
    --accent:#3a9fd6;
    --card-white:#ffffff;
  }
  *{box-sizing:border-box;margin:0;padding:0}
  html,body{width:704px;height:1200px;overflow:hidden}
  body{background:var(--page);position:relative;font-family:"Open Sans",Arial,sans-serif}

  .card{
    position:absolute;left:52px;width:600px;height:343px;
    border-radius:18px;overflow:hidden;
    box-shadow:0 6px 18px rgba(0,0,0,.18);
  }
  .card--front{top:150px;background:linear-gradient(180deg,var(--sky-pale) 0%,var(--sky) 45%,var(--leaf) 100%)}
  .card--back{top:707px;background:var(--card-white)}

  .wordmark{font-family:"Libre Baskerville",Georgia,serif;font-weight:700;color:var(--ink);line-height:1}
  .card--front .wordmark{position:absolute;right:40px;top:118px;text-align:right}
  .card--front .wordmark__name{display:block;font-size:50px;letter-spacing:1px}
  .card--front .wordmark__sub{display:block;font-size:21px;margin-top:8px;letter-spacing:1px}

  .back-band{position:absolute;left:0;top:0;width:100%;height:100%}

  .card--back .brand{position:absolute;left:34px;top:120px;display:flex;align-items:center;gap:12px}
  .brand__dot{width:30px;height:30px;border-radius:50%;background:var(--accent)}
  .card--back .wordmark__name{display:block;font-size:28px}
  .card--back .wordmark__sub{display:block;font-size:12px;margin-top:4px;letter-spacing:1px}

  .person{position:absolute;left:34px;top:218px}
  .person__name{color:var(--accent);font-size:18px;font-weight:400}
  .person__role{color:var(--text);font-size:14px;margin-top:2px}

  .contact{position:absolute;left:300px;top:196px;list-style:none}
  .contact__item{display:flex;align-items:center;gap:9px;font-size:13px;color:var(--text);height:24px}
  .contact__icon{width:14px;height:14px;flex:none}
</style>
</head>
<body>

  <section class="card card--front" aria-label="Card front">
    <div class="wordmark">
      <span class="wordmark__name">KEYSTONE</span>
      <span class="wordmark__sub">Endodontics P.C.</span>
    </div>
  </section>

  <section class="card card--back" aria-label="Card back">
    <svg class="back-band" viewBox="0 0 600 343" preserveAspectRatio="none" aria-hidden="true">
      <defs>
        <linearGradient id="bandSky" x1="0" y1="0" x2="0" y2="1">
          <stop offset="0" stop-color="#4fb3e3"/>
          <stop offset="1" stop-color="#8fd0ee"/>
        </linearGradient>
      </defs>
      <path d="M0 0 H600 V150 C500 110 430 60 300 85 C190 105 100 95 0 70 Z" fill="url(#bandSky)"/>
      <path d="M600 150 C500 110 430 60 300 85 C420 75 500 125 600 175 Z" fill="#8cc63f"/>
    </svg>

    <div class="brand">
      <span class="brand__dot"></span>
      <div class="wordmark">
        <span class="wordmark__name">KEYSTONE</span>
        <span class="wordmark__sub">Endodontics P.C.</span>
      </div>
    </div>

    <div class="person">
      <p class="person__name">Daniel Whitaker</p>
      <p class="person__role">Designation</p>
    </div>

    <ul class="contact">
      <li class="contact__item">
        <svg class="contact__icon" viewBox="0 0 14 14"><circle cx="7" cy="7" r="7" fill="#3a9fd6"/><path d="M4.5 3.5 6 3.5 6.6 5.3 5.7 6a5 5 0 0 0 2.3 2.3l.7-.9 1.8.6v1.5A1 1 0 0 1 9.5 10.5 6 6 0 0 1 3.5 4.5 1 1 0 0 1 4.5 3.5Z" fill="#fff"/></svg>
        (716)382-9157
      </li>
      <li class="contact__item">
        <svg class="contact__icon" viewBox="0 0 14 14"><circle cx="7" cy="7" r="7" fill="#3a9fd6"/><rect x="4" y="5" width="6" height="4" fill="#fff"/><rect x="5" y="3" width="4" height="2" fill="#fff"/></svg>
        (716)382-9150
      </li>
      <li class="contact__item">
        <svg class="contact__icon" viewBox="0 0 14 14"><circle cx="7" cy="7" r="7" fill="#3a9fd6"/><circle cx="7" cy="7" r="3.5" fill="none" stroke="#fff"/><path d="M3.5 7h7M7 3.5v7" stroke="#fff"/></svg>
        www.keystoneendo.com
      </li>
      <li class="contact__item">
        <svg class="contact__icon" viewBox="0 0 14 14"><circle cx="7" cy="7" r="7" fill="#3a9fd6"/><path d="M7 11 4.6 7.4A2.6 2.6 0 1 1 9.4 7.4Z" fill="#fff"/></svg>
        2847 Halloway Avenue, Suite K
      </li>
      <li class="contact__item" style="padding-left:23px">East Marlow, NY 14391</li>
    </ul>
  </section>

</body>
</html>
```